Velvet Lantern rebranding my business with a new business card

I have my new logo and now I need a refresher on my business cards. I really want something fun and fresh. I like black background or anything to make the color pop.
Logo
Name: Velvet Lantern
Contact Info as stated below:
Mara Pelkin
519-555-0147
Logo
Name: Velvet Lantern
Mara Pelkin
519-555-0147
fb.me/VelvetLanternbyMara
Instagram: @VelvetLanternbyMara

Industry/Entity Type

Business

Contact Information for Business Card

double-sided. Logo on one side. Contact info on the other.

Requirements
Must have
• Logo
• Name: Velvet Lantern
• Contact Info as stated below:
• Mara Pelkin
• 519-555-0147
• fb.me/VelvetLanternbyMara
• fb.me/VelvetLanternbyMara

```html
<!DOCTYPE html>
<html lang="en">
<head>
<meta charset="utf-8">
<title>Velvet Lantern — Business Card</title>
<link rel="stylesheet" href="https://fonts.googleapis.com/css2?family=Roboto:wght@400;500;700&display=swap">
<style>
  :root {
    --stage: #e9e6e1;
    --card-light: #f7f7f5;
    --card-dark: #1f2022;
    --ink-grey: #5c5c5c;
    --ink-white: #ffffff;
    --ring-pink: #f0a9bf;
    --ring-dark: #1a1a1a;
  }
  * { box-sizing: border-box; margin: 0; padding: 0; }
  html, body {
    width: 1200px; height: 960px; overflow: hidden;
    background: var(--stage);
    font-family: "Roboto", Arial, sans-serif;
  }
  .canvas { position: relative; width: 1200px; height: 960px; }

  .card {
    position: absolute; left: 320px; width: 600px;
    border-radius: 18px;
    box-shadow: 0 4px 14px rgba(0,0,0,.18);
  }
  .card--front { top: 95px; height: 360px; background: var(--card-light); }
  .card--back  { top: 492px; height: 343px; background: var(--card-dark); }

  .brand-seal {
    position: absolute; left: 193px; top: 74px;
    width: 206px; height: 206px; border-radius: 50%;
    background: #fff;
    border: 2px solid var(--ring-dark);
    box-shadow: inset 0 0 0 5px #fff, inset 0 0 0 7px var(--ring-pink);
    display: flex; align-items: center; justify-content: center;
  }
  .brand-seal__name {
    font-weight: 700; font-size: 20px; color: var(--ring-dark);
    text-align: center; line-height: 1.2; text-transform: uppercase;
  }
  .front-url {
    position: absolute; left: 0; right: 0; top: 316px;
    text-align: center; font-size: 14px; letter-spacing: 5.2px;
    color: var(--ink-grey);
  }

  .back-brand {
    position: absolute; right: 30px; top: 150px;
    font-weight: 700; font-size: 34px; color: var(--ink-white);
    text-transform: uppercase; letter-spacing: 1px;
  }
  .contact { position: absolute; left: 32px; top: 218px; color: var(--ink-white); }
  .contact__name { font-weight: 500; font-size: 20px; margin-bottom: 12px; text-transform: uppercase; }
  .contact__list { list-style: none; }
  .contact__item {
    display: flex; align-items: center; gap: 8px;
    font-size: 14.5px; line-height: 19.5px;
  }
  .contact__icon { width: 13px; height: 13px; fill: var(--ink-white); flex: none; }
</style>
</head>
<body>
<main class="canvas">
  <section class="card card--front" aria-label="Card front">
    <div class="brand-seal">
      <span class="brand-seal__name">Velvet<br>Lantern</span>
    </div>
    <p class="front-url">www.velvetlantern.com</p>
  </section>

  <section class="card card--back" aria-label="Card back">
    <p class="back-brand">Velvet Lantern</p>
    <div class="contact">
      <p class="contact__name">Mara Pelkin</p>
      <ul class="contact__list">
        <li class="contact__item">
          <svg class="contact__icon" viewBox="0 0 24 24" aria-hidden="true"><path d="M6.6 10.8a15.1 15.1 0 0 0 6.6 6.6l2.2-2.2c.3-.3.7-.4 1-.2 1.1.4 2.3.6 3.6.6.6 0 1 .4 1 1V20c0 .6-.4 1-1 1A17 17 0 0 1 3 4c0-.6.4-1 1-1h3.5c.6 0 1 .4 1 1 0 1.3.2 2.5.6 3.6.1.3 0 .7-.2 1z"/></svg>
          519-555-0147
        </li>
        <li class="contact__item">
          <svg class="contact__icon" viewBox="0 0 24 24" aria-hidden="true"><circle cx="12" cy="12" r="10" fill="none" stroke="#fff" stroke-width="2.4"/><path d="M2 12h20M12 2c3 3 3 17 0 20M12 2c-3 3-3 17 0 20" fill="none" stroke="#fff" stroke-width="2"/></svg>
          www.velvetlantern.com
        </li>
        <li class="contact__item">
          <svg class="contact__icon" viewBox="0 0 24 24" aria-hidden="true"><path d="M4 3h16a2 2 0 0 1 2 2v10a2 2 0 0 1-2 2H9l-5 4v-4a2 2 0 0 1-2-2V5a2 2 0 0 1 2-2z"/></svg>
          fb.me/VelvetLanternbyMara
        </li>
      </ul>
    </div>
  </section>
</main>
</body>
</html>
```